Simple Print Ad for Nonprofit Crisis Call Line

Nonprofit agency needs a simple ad FOR PRINT PUBLICATIONS (newspapers, magazines, etc.) to advertise its Crisis Call Line. Ad should be GRAPHICALLY SIMPLE and bold, eye-catching, and easily increased/decreased in size. The graphic format needs to be at least 300 DPI and should be in both a jpeg and pdf. We will need color and black and white versions.

SIZE OF AD: Since the ad will appear in multiple publications, the ads need to be scalable, or easily increased/decreased in size to increase the chances that publications will place them and to avoid having to have dozens of individually designed ads.

For the purpose of the initial ad design, please design a horizontal ad that is close to 4" tall and 5" long and a vertical ad that is 21/2" wide by 41/2" long. The winning artist will need to provide us will all the ad elements as separate files so that they can be manipulated to produce different size ads. The artist may also be asked to make additional ads in different sizes and languages in the future.
Updates

Thank you to everyone that has submitted a design. We are in the process of reviewing the designs and compiling our comments and questions. Please give us a few days to respond.

Industry/Entity Type

Call

Requirements
Must have
• Agency logo and the text included.
Should not have
• Any other text other than what is provided.

```html
<!DOCTYPE html>
<html lang="en">
<head>
<meta charset="utf-8">
<title>The Crisis Line – Print Ads</title>
<link href="https://fonts.googleapis.com/css2?family=Arvo:wght@700&family=Roboto+Condensed:wght@700&family=Roboto:wght@300;400;700&display=swap" rel="stylesheet">
<style>
  :root {
    --page-bg: #5a5a5a;
    --brand-green: #22a83a;
    --lime: #c8dc1e;
    --slate: #5e6268;
    --wave-grey: #8a8d92;
    --white: #ffffff;
    --photo-light: #e6e6e6;
    --photo-mid: #b9b9b9;
  }
  * { margin: 0; padding: 0; box-sizing: border-box; }
  html, body { width: 1200px; height: 900px; overflow: hidden; }
  body {
    background: var(--page-bg);
    font-family: "Roboto", Arial, sans-serif;
    position: relative;
  }
  .ad { position: absolute; overflow: hidden; background: var(--brand-green); }
  .tagline {
    color: var(--white);
    font-family: "Roboto Condensed", "Arial Narrow", sans-serif;
    font-weight: 700;
  }
  .tagline span { display: block; white-space: nowrap; }
  .note { color: var(--white); font-weight: 300; white-space: nowrap; }
  .slab { font-family: "Arvo", Georgia, serif; font-weight: 700; color: var(--white); white-space: nowrap; }

  /* ---------- Vertical ad ---------- */
  .ad-vertical { left: 110px; top: 100px; width: 390px; height: 700px; }
  .ad-vertical .photo {
    position: absolute; left: 0; top: 0; width: 100%; height: 300px;
    background: linear-gradient(120deg, var(--photo-light) 0%, var(--photo-mid) 70%, #6a5a50 100%);
  }
  .ad-vertical .swoosh {
    position: absolute; left: 0; top: 300px; width: 100%; height: 90px;
    background: linear-gradient(180deg, var(--photo-mid) 0%, var(--wave-grey) 35%, var(--lime) 65%, var(--brand-green) 100%);
  }
  .ad-vertical .agency-mark {
    position: absolute; left: 22px; top: 20px; width: 118px; height: 100px;
    background: var(--white); display: flex; flex-direction: column;
    align-items: center; justify-content: center; gap: 8px; padding: 8px;
  }
  .ad-vertical .tagline {
    position: absolute; left: 32px; top: 402px;
    font-size: 36px; line-height: 1.1;
  }
  .ad-vertical .tagline .l2 { padding-left: 18px; }
  .ad-vertical .tagline .l3 { padding-left: 96px; }
  .ad-vertical .note { position: absolute; left: 96px; top: 540px; font-size: 21px; }
  .ad-vertical .name-band {
    position: absolute; left: 0; top: 592px; width: 100%; height: 52px;
    background: var(--slate); font-size: 30px;
    display: flex; align-items: center; justify-content: center;
  }
  .ad-vertical .phone {
    position: absolute; left: 0; top: 644px; width: 100%; height: 56px;
    display: flex; align-items: center; justify-content: center; gap: 8px;
    font-size: 32px;
  }

  /* ---------- Horizontal ad ---------- */
  .ad-horizontal { left: 570px; top: 160px; width: 520px; height: 580px; }
  .ad-horizontal .photo {
    position: absolute; left: 0; top: 14px; width: 100%; height: 226px;
    background: linear-gradient(100deg, #d9dde0 0%, #f4f4f4 45%, #e7c6c0 80%, #d24a66 100%);
  }
  .ad-horizontal .agency-mark {
    position: absolute; right: 26px; top: 170px; width: 130px; height: 150px;
    background: var(--white); border: 4px solid var(--brand-green);
    display: flex; flex-direction: column; align-items: center; justify-content: center; gap: 10px; padding: 8px;
  }
  .ad-horizontal .tagline {
    position: absolute; left: 28px; top: 250px;
    font-size: 32px; line-height: 1.1;
  }
  .ad-horizontal .tagline .l2 { padding-left: 14px; }
  .ad-horizontal .tagline .l3 { padding-left: 70px; }
  .ad-horizontal .note { position: absolute; left: 110px; top: 378px; font-size: 18px; }
  .ad-horizontal .call-band {
    position: absolute; left: 0; top: 410px; width: 100%; height: 122px;
    background: var(--slate);
  }
  .ad-horizontal .line-name { position: absolute; left: 96px; top: 12px; font-size: 22px; }
  .ad-horizontal .phone-number { position: absolute; left: 54px; top: 50px; font-size: 40px; }

  /* ---------- Agency name stand-in ---------- */
  .agency-square { width: 22px; height: 22px; background: var(--brand-green); }
  .agency-name {
    font-family: "Roboto", Arial, sans-serif; font-weight: 700;
    color: var(--brand-green); font-size: 15px; line-height: 1.15; text-align: center;
  }
</style>
</head>
<body>

  <article class="ad ad-vertical">
    <div class="photo" role="img" aria-label="Photo of a worried woman talking on a mobile phone"></div>
    <div class="swoosh" role="img" aria-label="Decorative green, grey and lime wave band"></div>
    <div class="agency-mark">
      <div class="agency-square"></div>
      <div class="agency-name">Harbor Family Service</div>
    </div>
    <h2 class="tagline">
      <span class="l1">Any person,</span>
      <span class="l2">any problem,</span>
      <span class="l3">any time.</span>
    </h2>
    <p class="note">Free and confidential.</p>
    <div class="name-band slab">The Crisis Line</div>
    <div class="phone slab">
      <svg width="30" height="30" viewBox="0 0 30 30" aria-hidden="true">
        <circle cx="15" cy="15" r="13" fill="none" stroke="var(--white)" stroke-width="2.5"/>
        <path d="M10 8 l3 0 l1.5 4 l-2 1.5 c1 2.2 2.2 3.4 4 4.2 l1.5 -2 l4 1.5 l0 3 c-6 1 -12.5 -5.5 -12 -12.2 z" fill="var(--white)"/>
      </svg>
      <span>615-555-0148</span>
    </div>
  </article>

  <article class="ad ad-horizontal">
    <div class="photo" role="img" aria-label="Photo of a young girl smiling with her parents talking in the background"></div>
    <div class="agency-mark">
      <div class="agency-square"></div>
      <div class="agency-name">Harbor Family Service</div>
    </div>
    <h2 class="tagline">
      <span class="l1">Any person,</span>
      <span class="l2">any problem,</span>
      <span class="l3">any time.</span>
    </h2>
    <p class="note">Free and confidential.</p>
    <div class="call-band">
      <p class="line-name slab">The Crisis Line</p>
      <p class="phone-number slab">615-555-0148</p>
    </div>
  </article>

</body>
</html>
```